K3 Construction Site Sign

I would like to get a sign designed which would be installed at a construction sign. I would like to incorporate my current logo, font and colors in the sign. The sign would be 30" x 60" (vertical). Would like to keep it clean and simple yet eye catching and sparks interest. I have attached my branding colors. I would like the background to be the branded blue with white text.

```html
<!DOCTYPE html>
<html lang="en">
<head>
<meta charset="utf-8">
<title>K3 Buildworks Inc. – Site Sign</title>
<link href="https://fonts.googleapis.com/css2?family=Roboto+Condensed:wght@400;700&display=swap" rel="stylesheet">
<style>
  :root {
    --backdrop: #6b6b6b;
    --brand-orange: #fbb040;
    --brand-blue: #0c55a5;
    --white: #ffffff;
  }
  html, body {
    margin: 0;
    padding: 0;
    width: 1200px;
    height: 1200px;
    overflow: hidden;
    background: var(--backdrop);
  }
  .sign {
    position: absolute;
    left: 320px;
    top: 40px;
    width: 560px;
    height: 1120px;
    font-family: "Roboto Condensed", Arial, sans-serif;
  }
  .sign__header {
    position: absolute;
    left: 0; top: 0;
    width: 100%;
    height: 400px;
    background: var(--brand-orange);
  }
  .brand {
    position: absolute;
    left: 88px;
    top: 300px;
    display: flex;
    align-items: center;
    gap: 18px;
  }
  .brand__square {
    width: 44px;
    height: 44px;
    background: var(--white);
  }
  .brand__name {
    color: var(--white);
    font-weight: 400;
    font-size: 38px;
    line-height: 44px;
    letter-spacing: 1px;
    white-space: nowrap;
  }
  .sign__body {
    position: absolute;
    left: 0; top: 400px;
    width: 100%;
    height: 720px;
    background: var(--brand-blue);
  }
  .services {
    list-style: none;
    margin: 0;
    padding: 0;
    position: absolute;
    left: 67px;
    top: 48px;
  }
  .service {
    position: relative;
    padding-left: 40px;
    font-size: 45px;
    line-height: 55px;
    color: var(--white);
    margin-bottom: 12px;
  }
  .service--accent { color: var(--brand-orange); }
  .service::before {
    content: "";
    position: absolute;
    left: 0;
    top: 15px;
    width: 26px;
    height: 26px;
    background: var(--brand-orange);
  }
  .service--accent::before { background: var(--white); }
  .service--wrap { margin-bottom: 20px; }
  .sign__rule {
    position: absolute;
    left: 65px;
    top: 607px;
    width: 430px;
    height: 4px;
    background: var(--brand-orange);
  }
  .sign__url {
    position: absolute;
    left: 65px;
    top: 630px;
    width: 430px;
    text-align: center;
    font-weight: 700;
    font-size: 50px;
    line-height: 60px;
    color: var(--white);
    letter-spacing: 0.5px;
    white-space: nowrap;
  }
</style>
</head>
<body>
  <main class="sign">
    <header class="sign__header">
      <div class="brand">
        <span class="brand__square"></span>
        <span class="brand__name">K3 BUILDWORKS INC.</span>
      </div>
    </header>
    <section class="sign__body">
      <ul class="services">
        <li class="service">Custom Homes</li>
        <li class="service service--accent">Multi-Family</li>
        <li class="service">Tenant Improvements</li>
        <li class="service service--accent service--wrap">Commercial/Office<br>Renovations</li>
        <li class="service">Property Development<br>Consulting</li>
      </ul>
      <div class="sign__rule"></div>
      <div class="sign__url">K3BUILDWORKS.CA</div>
    </section>
  </main>
</body>
</html>
```